Business Card for Brevel Coatings

We need a simple, yet out standing business card for our painting company.

Target Market(s)

wealthy; high-end neighborhoods, and businesses

Industry/Entity Type

Painting

Contact Information for Business Card

Name:
Doran Vask

Email:
d.vask@brevel-coatings.com

Website:
Brevel-coatings.com

Phone Number:
(555) 416-9073

Font styles to use
Serif
Sans Serif

Requirements
Must have
• slogan "making spaces shine"
Should not have
• A title attached to the name on the card

```html
<!DOCTYPE html>
<html lang="en">
<head>
<meta charset="utf-8">
<title>Brevel Coatings — Business Card</title>
<link rel="stylesheet" href="https://fonts.googleapis.com/css2?family=Open+Sans:wght@400;600;700&family=Cinzel:wght@400&display=swap">
<style>
  :root {
    --bg: #d9d6d0;
    --card-light: #f1f2f0;
    --card-light-edge: #dcdedb;
    --lime: #a6c33a;
    --forest: #3f5a1f;
    --sage: #8ea66a;
    --ink: #2f3033;
    --ink-soft: #55585c;
    --black: #050505;
    --charcoal: #3a3b3c;
    --white: #ffffff;
  }
  * { margin: 0; padding: 0; box-sizing: border-box; }
  html, body { width: 1200px; height: 800px; overflow: hidden; }
  body {
    background: var(--bg);
    font-family: "Open Sans", Arial, sans-serif;
    position: relative;
  }
  .card {
    position: absolute;
    top: 246px;
    width: 540px;
    height: 308px;
    border-radius: 4px;
    overflow: hidden;
    box-shadow: 0 10px 28px rgba(0,0,0,0.22);
  }
  /* Front */
  .card-front {
    left: 40px;
    background: linear-gradient(180deg, var(--card-light) 0%, var(--card-light-edge) 100%);
  }
  .card-front .band { position: absolute; inset: 0; }
  .brand-mark {
    position: absolute;
    top: 28px;
    right: 34px;
  }
  .brand-mark .brand-line {
    display: flex;
    align-items: center;
    gap: 8px;
  }
  .brand-mark .brand-square {
    width: 14px; height: 14px;
    background: var(--lime);
  }
  .brand-mark .brand-name {
    font-family: "Cinzel", Georgia, serif;
    font-size: 19px;
    color: var(--forest);
    letter-spacing: 1px;
    white-space: nowrap;
  }
  .brand-mark .slogan {
    margin-top: 3px;
    margin-left: 22px;
    font-size: 10px;
    color: var(--forest);
    letter-spacing: 0.3px;
  }
  .holder-name {
    position: absolute;
    left: 186px;
    top: 82px;
    font-size: 27px;
    font-weight: 700;
    color: var(--ink);
    white-space: nowrap;
  }
  .contact {
    position: absolute;
    font-size: 13px;
    color: var(--ink-soft);
    white-space: nowrap;
  }
  .contact-phone { left: 34px; top: 188px; }
  .contact-web { left: 186px; top: 188px; }
  .contact-mail { left: 334px; top: 162px; }
  /* Back */
  .card-back {
    left: 620px;
    background: linear-gradient(112deg, var(--black) 0%, #0b0b0b 52%, #1c1c1c 60%, var(--charcoal) 66%, var(--charcoal) 100%);
  }
  .card-back .accent { position: absolute; }
  .accent-top { top: 0; right: 96px; width: 48px; height: 10px; background: var(--lime); }
  .accent-right { top: 0; right: 0; width: 10px; height: 308px; background: var(--sage); }
  .accent-bottom { bottom: 0; right: 0; width: 300px; height: 9px; background: var(--lime); }
  .accent-left { bottom: 34px; left: 0; width: 10px; height: 36px; background: var(--sage); }
  .back-brand {
    position: absolute;
    left: 0; right: 0;
    top: 132px;
    display: flex;
    justify-content: center;
    align-items: center;
    gap: 14px;
  }
  .back-brand .brand-square {
    width: 22px; height: 22px;
    background: var(--white);
  }
  .back-brand .brand-name {
    font-family: "Cinzel", Georgia, serif;
    font-size: 30px;
    color: var(--white);
    letter-spacing: 4px;
    white-space: nowrap;
  }
</style>
</head>
<body>
  <section class="card card-front" aria-label="Business card front">
    <svg class="band" width="540" height="308" viewBox="0 0 540 308">
      <polygon points="300,150 318,124 540,124 540,150" fill="var(--forest)"/>
      <polygon points="0,150 300,150 312,176 0,176" fill="var(--lime)"/>
      <polygon points="300,150 318,124 330,150 312,176" fill="var(--forest)"/>
      <g transform="translate(50,163)">
        <polygon points="-12,0 -6,-11 6,-11 12,0 6,11 -6,11" fill="var(--white)"/>
        <path d="M-4,-5 q-2,6 4,10 l2,-2 -2,-3 -1,1 q-2,-2 -2,-4 l1,-1 -2,-3z" fill="var(--forest)"/>
      </g>
      <g transform="translate(202,163)">
        <polygon points="-12,0 -6,-11 6,-11 12,0 6,11 -6,11" fill="var(--white)"/>
        <circle r="6" fill="none" stroke="var(--forest)" stroke-width="1.3"/>
        <ellipse rx="2.6" ry="6" fill="none" stroke="var(--forest)" stroke-width="1"/>
        <line x1="-6" y1="0" x2="6" y2="0" stroke="var(--forest)" stroke-width="1"/>
      </g>
      <g transform="translate(350,137)">
        <polygon points="-12,0 -6,-11 6,-11 12,0 6,11 -6,11" fill="var(--white)"/>
        <rect x="-6" y="-4" width="12" height="8" fill="none" stroke="var(--forest)" stroke-width="1.2"/>
        <polyline points="-6,-4 0,1 6,-4" fill="none" stroke="var(--forest)" stroke-width="1.2"/>
      </g>
    </svg>
    <div class="brand-mark">
      <div class="brand-line"><span class="brand-square"></span><span class="brand-name">Brevel Coatings</span></div>
      <div class="slogan">making spaces shine</div>
    </div>
    <div class="holder-name">Doran Vask</div>
    <div class="contact contact-phone">(555) 416-9073</div>
    <div class="contact contact-web">Brevel-coatings.com</div>
    <div class="contact contact-mail">d.vask@brevel-coatings.com</div>
  </section>

  <section class="card card-back" aria-label="Business card back">
    <span class="accent accent-top"></span>
    <span class="accent accent-right"></span>
    <span class="accent accent-bottom"></span>
    <span class="accent accent-left"></span>
    <div class="back-brand">
      <span class="brand-square"></span>
      <span class="brand-name">BREVEL COATINGS</span>
    </div>
  </section>
</body>
</html>
```